Start-up lawncare company needing marketing flyer to promote business model

Hello! We are looking for a marketing flyer design with the requirements below.

We would like the size to fit a flyer that is 6.25" X 9", Front and Back.

We need these to meet the KBMR ORTQ requirements, there are details attached for the indicias that need to be included, and where to put them on the back of the flyer.

Here's the items items we would like to have included on the flyer:
- Logo (Attached)

- I attached a snip of how our website looks, as well as how our app looks, and would like to follow that general color scheme

- References to our Fernquill App, in both Zenthra and Vorby stores, and our website (www.Fernquill.com)

- Reference to the neighborhood barometer and gets the point across that the more of their neighbors that sign up, the cheaper the price of service (Visual attached of what this barometer looks like)

- We are licensed and insured landscaping pros

- Real, instant, upfront pricing for mowing, mulching and most other services

- Sign up with a few easy steps and manage your account from our app or online

- Automated safe & secure transactions upon service completion and satisfaction

- Excellent customer service with our quality guaranteed commitment!

- Sign up now and receive 50% off your first mow!

- Veteran owned

- A portion of our proceeds go to "Rennick Dolby Foundation"

- List's out all of the services we will offer
- Mowing
- Mulching
- Aeration and Over-seeding
- Fertilization
- Shrub/Tree Trimming
- Leaf removal and yard clean up
- Accent lighting installation
- Sprinkler blow-out / Winterization
- Driveway pressure washing and sealing
- Firewood Delivery

Target Market(s)

Homeowners in large neighborhoods that need lawn care services

Industry/Entity Type

Lawn Care

Font styles to use
Sans Serif

Colors

Designer to choose colors to be used in the design.

Requirements
Must have
• Meet KBMR ORTQ requirements
• Keep a similar color scheme to our website, feel free to use bold accents to make it more eye-catching as people search through their mail
• Get the general point across that as more of their neighbors sign up with us, the cheaper their service will be

```html
<!DOCTYPE html>
<html lang="en">
<head>
<meta charset="utf-8">
<title>Fernquill Mailer – Front and Back</title>
<link rel="stylesheet" href="https://fonts.googleapis.com/css2?family=Bebas+Neue&family=Cabin:wght@400;600;700&family=Arimo:wght@400;700&display=swap">
<style>
:root{
  --bg:#dcdcdc;
  --white:#ffffff;
  --green:#3bb54a;
  --green-deep:#1f8f3a;
  --blue:#27a3dc;
  --navy:#2c4597;
  --red:#e31e24;
  --yellow:#ffe600;
  --ink:#1e2a44;
  --ink-soft:#2b3a55;
  --black:#111111;
}
*{margin:0;padding:0;box-sizing:border-box}
html,body{width:1200px;height:1200px;overflow:hidden;background:var(--bg)}
body{position:relative;font-family:'Cabin',sans-serif}
.card{position:absolute;left:268px;width:665px;height:467px;background:var(--white);overflow:hidden}
.card--front{top:92px}
.card--back{top:635px}

/* front */
.front-field{position:absolute;left:175px;top:0;right:0;bottom:0;
  background:linear-gradient(100deg,var(--blue) 0%,#35b6a0 40%,var(--green) 75%);
  border-bottom-left-radius:42px}
.front-topwhite{position:absolute;left:0;top:0;width:175px;height:318px;background:var(--white)}
.hero-frame{position:absolute;left:17px;top:19px;width:632px;height:302px;
  border:2px solid var(--white);border-left-color:var(--green);border-top-color:var(--green);
  border-top-left-radius:30px;border-bottom-right-radius:30px}
.hero-photo{position:absolute;left:21px;top:23px;width:624px;height:252px;border-top-left-radius:28px;
  background:linear-gradient(100deg,#e39a3a 0%,#c05a3c 28%,#8a9a3a 55%,#c9c43a 70%,#4f8f2e 100%)}
.licensed-band{position:absolute;left:21px;top:274px;width:624px;height:45px;background:var(--navy);
  border-bottom-right-radius:28px;color:var(--white);font-family:'Bebas Neue',sans-serif;
  font-size:29px;letter-spacing:.2px;line-height:45px;padding-left:18px}
.offer{position:absolute;left:481px;top:14px;width:139px;height:129px;background:var(--red);
  border-radius:12px;text-align:center;color:var(--white);padding-top:14px}
.offer__lead{font-size:16px;line-height:17px;font-family:'Cabin',sans-serif}
.offer__pct{font-family:'Bebas Neue',sans-serif;color:var(--yellow);font-size:52px;line-height:44px;margin-top:2px}
.offer__pct span{font-family:'Cabin',sans-serif;font-weight:700;color:var(--white);font-size:17px;vertical-align:top;line-height:24px}
.offer__tail{font-family:'Bebas Neue',sans-serif;font-size:23px;line-height:24px}
.app-screen{position:absolute;left:498px;top:184px;width:132px;height:276px;border-radius:18px;
  background:linear-gradient(170deg,#2a2a2a 0%,#3a9a55 18%,#2fa04a 75%,#2c4597 88%,#222 100%);
  transform:rotate(8deg)}
.brand{position:absolute;font-family:'Bebas Neue',sans-serif;color:var(--navy);display:flex;align-items:center;gap:6px}
.brand__mark{width:14px;height:14px;background:var(--green)}
.brand--front{left:28px;top:376px;font-size:38px}
.perks{position:absolute;left:197px;top:336px;list-style:none;font-size:8px;color:var(--ink)}
.perks li{height:18px;line-height:18px;display:flex;align-items:center;gap:5px}
.tick{width:8px;height:8px;flex:none}

/* back */
.back-field{position:absolute;left:0;top:0;width:390px;height:244px;
  background:linear-gradient(120deg,var(--green) 30%,#2aa6d4 80%,var(--blue));border-bottom-right-radius:42px}
.back-photo{position:absolute;left:358px;top:0;right:0;height:244px;
  background:linear-gradient(140deg,#5f9a38 0%,#3f7a2a 45%,#7aa84a 75%,#355f2a 100%);border-bottom-left-radius:42px}
.services-title{position:absolute;left:34px;top:24px;font-family:'Bebas Neue',sans-serif;font-weight:400;color:var(--white);
  font-size:29px;line-height:31px}
.services{position:absolute;top:98px;list-style:none;color:var(--white);font-size:9px}
.services li{height:15px;line-height:15px;display:flex;align-items:center;gap:4px}
.services--a{left:34px}
.services--b{left:163px}
.barometer-note{position:absolute;left:34px;top:186px;width:320px;color:var(--white);
  font-size:10px;font-weight:700;line-height:13px;display:flex;align-items:center;gap:5px}
.barometer-note .tick{width:9px;height:9px}
.brand--back{left:104px;top:266px;font-size:34px}
.web-box{position:absolute;left:28px;top:341px;width:310px;height:56px;border:1.2px solid var(--ink-soft);
  border-radius:9px;text-align:center;padding-top:5px}
.web-box__cta{font-weight:600;font-size:15px;color:var(--navy)}
.web-box__cta em{font-style:normal;color:var(--green-deep)}
.web-box__url{font-weight:600;font-size:13.5px;letter-spacing:1.6px;color:var(--ink);margin-top:1px}
.store{position:absolute;top:410px;height:29px;background:var(--black);border-radius:4px;color:var(--white);
  font-family:'Cabin',sans-serif;font-size:13px;display:flex;align-items:center;justify-content:center;gap:5px}
.store--z{left:90px;width:86px}
.store--v{left:184px;width:99px}
.indicia{position:absolute;left:579px;top:281px;width:54px;height:54px;border:1px solid #333;
  font-family:'Arimo',sans-serif;font-size:7px;line-height:8.6px;text-align:center;padding-top:4px;color:#222}
.address{position:absolute;left:432px;top:363px;width:180px;height:72px;border:1px solid #555;
  font-family:'Arimo',sans-serif;color:#222;padding:8px 0 0 13px}
.address__route{font-size:8px;padding-left:40px}
.address__name{font-size:11px;line-height:12px;margin-top:14px}
</style>
</head>
<body>

<section class="card card--front">
  <div class="front-field"></div>
  <div class="front-topwhite"></div>
  <div class="hero-frame"></div>
  <div class="hero-photo" role="img" aria-label="Photo of a landscaper in a cap checking a tablet among colourful garden shrubs"></div>
  <div class="licensed-band">We are licensed and insured landscaping pros</div>
  <div class="offer">
    <div class="offer__lead">SIGN UP NOW<br>AND RECEIVE</div>
    <div class="offer__pct">50%<span>OFF</span></div>
    <div class="offer__tail">YOUR FIRST MOW</div>
  </div>
  <div class="brand brand--front"><span class="brand__mark"></span>Fernquill</div>
  <ul class="perks">
    <li><svg class="tick" viewBox="0 0 10 10"><circle cx="5" cy="5" r="4.3" fill="none" stroke="#1e2a44" stroke-width=".9"/><path d="M3 5.2l1.5 1.4L7.2 3.8" fill="none" stroke="#1e2a44" stroke-width=".9"/></svg>Real, instant, upfront pricing for mowing, mulching and most other services</li>
    <li><svg class="tick" viewBox="0 0 10 10"><circle cx="5" cy="5" r="4.3" fill="none" stroke="#1e2a44" stroke-width=".9"/><path d="M3 5.2l1.5 1.4L7.2 3.8" fill="none" stroke="#1e2a44" stroke-width=".9"/></svg>Sign up with a few easy steps and manage your account from our app or online</li>
    <li><svg class="tick" viewBox="0 0 10 10"><circle cx="5" cy="5" r="4.3" fill="none" stroke="#1e2a44" stroke-width=".9"/><path d="M3 5.2l1.5 1.4L7.2 3.8" fill="none" stroke="#1e2a44" stroke-width=".9"/></svg>Automated safe &amp; secure transactions upon service completion and satisfaction</li>
    <li><svg class="tick" viewBox="0 0 10 10"><circle cx="5" cy="5" r="4.3" fill="none" stroke="#1e2a44" stroke-width=".9"/><path d="M3 5.2l1.5 1.4L7.2 3.8" fill="none" stroke="#1e2a44" stroke-width=".9"/></svg>Excellent customer service with our quality guaranteed commitment!</li>
    <li><svg class="tick" viewBox="0 0 10 10"><circle cx="5" cy="5" r="4.3" fill="none" stroke="#1e2a44" stroke-width=".9"/><path d="M3 5.2l1.5 1.4L7.2 3.8" fill="none" stroke="#1e2a44" stroke-width=".9"/></svg>Veteran owned</li>
    <li><svg class="tick" viewBox="0 0 10 10"><circle cx="5" cy="5" r="4.3" fill="none" stroke="#1e2a44" stroke-width=".9"/><path d="M3 5.2l1.5 1.4L7.2 3.8" fill="none" stroke="#1e2a44" stroke-width=".9"/></svg>A portion of our proceeds go to "Rennick Dolby Foundation"</li>
  </ul>
  <div class="app-screen" role="img" aria-label="Smartphone showing the instant quote screen of the app with mowing, mulching and additional services options"></div>
</section>

<section class="card card--back">
  <div class="back-photo" role="img" aria-label="Photo of a gardener trimming a green hedge with a power hedge trimmer"></div>
  <div class="back-field"></div>
  <h2 class="services-title">List's out all of the<br>services we will offer</h2>
  <ul class="services services--a">
    <li><svg class="tick" viewBox="0 0 10 10"><circle cx="5" cy="5" r="4.3" fill="none" stroke="#fff" stroke-width=".9"/><path d="M3 5.2l1.5 1.4L7.2 3.8" fill="none" stroke="#fff" stroke-width=".9"/></svg>Mowing</li>
    <li><svg class="tick" viewBox="0 0 10 10"><circle cx="5" cy="5" r="4.3" fill="none" stroke="#fff" stroke-width=".9"/><path d="M3 5.2l1.5 1.4L7.2 3.8" fill="none" stroke="#fff" stroke-width=".9"/></svg>Mulching</li>
    <li><svg class="tick" viewBox="0 0 10 10"><circle cx="5" cy="5" r="4.3" fill="none" stroke="#fff" stroke-width=".9"/><path d="M3 5.2l1.5 1.4L7.2 3.8" fill="none" stroke="#fff" stroke-width=".9"/></svg>Aeration and Over-seeding</li>
    <li><svg class="tick" viewBox="0 0 10 10"><circle cx="5" cy="5" r="4.3" fill="none" stroke="#fff" stroke-width=".9"/><path d="M3 5.2l1.5 1.4L7.2 3.8" fill="none" stroke="#fff" stroke-width=".9"/></svg>Fertilization</li>
    <li><svg class="tick" viewBox="0 0 10 10"><circle cx="5" cy="5" r="4.3" fill="none" stroke="#fff" stroke-width=".9"/><path d="M3 5.2l1.5 1.4L7.2 3.8" fill="none" stroke="#fff" stroke-width=".9"/></svg>Shrub/Tree Trimming</li>
  </ul>
  <ul class="services services--b">
    <li><svg class="tick" viewBox="0 0 10 10"><circle cx="5" cy="5" r="4.3" fill="none" stroke="#fff" stroke-width=".9"/><path d="M3 5.2l1.5 1.4L7.2 3.8" fill="none" stroke="#fff" stroke-width=".9"/></svg>Leaf removal and yard clean up</li>
    <li><svg class="tick" viewBox="0 0 10 10"><circle cx="5" cy="5" r="4.3" fill="none" stroke="#fff" stroke-width=".9"/><path d="M3 5.2l1.5 1.4L7.2 3.8" fill="none" stroke="#fff" stroke-width=".9"/></svg>Accent lighting installation</li>
    <li><svg class="tick" viewBox="0 0 10 10"><circle cx="5" cy="5" r="4.3" fill="none" stroke="#fff" stroke-width=".9"/><path d="M3 5.2l1.5 1.4L7.2 3.8" fill="none" stroke="#fff" stroke-width=".9"/></svg>Sprinkler blow-out / Winterization</li>
    <li><svg class="tick" viewBox="0 0 10 10"><circle cx="5" cy="5" r="4.3" fill="none" stroke="#fff" stroke-width=".9"/><path d="M3 5.2l1.5 1.4L7.2 3.8" fill="none" stroke="#fff" stroke-width=".9"/></svg>Driveway pressure washing and sealing</li>
    <li><svg class="tick" viewBox="0 0 10 10"><circle cx="5" cy="5" r="4.3" fill="none" stroke="#fff" stroke-width=".9"/><path d="M3 5.2l1.5 1.4L7.2 3.8" fill="none" stroke="#fff" stroke-width=".9"/></svg>Firewood Delivery</li>
  </ul>
  <p class="barometer-note"><svg class="tick" viewBox="0 0 10 10"><path d="M5 9V1.5M2 4.5L5 1.5l3 3" fill="none" stroke="#fff" stroke-width="1.2"/></svg>The more neighbors who sign up, the cheaper your service gets!</p>
  <div class="brand brand--back"><span class="brand__mark"></span>Fernquill</div>
  <div class="web-box">
    <div class="web-box__cta">VISIT OUR WEBSITE &amp; <em>SIGN UP NOW</em></div>
    <div class="web-box__url">www.Fernquill.com</div>
  </div>
  <div class="store store--z">Zenthra</div>
  <div class="store store--v">Vorby</div>
  <div class="indicia">PRSRT STD<br>ECRWSS<br>U.S. Postage<br><b>PAID</b><br>ORTQ RETAIL</div>
  <div class="address">
    <div class="address__route">****************ECRWSS****</div>
    <div class="address__name">Local<br>Postal Customer</div>
  </div>
</section>

</body>
</html>
```